Private Practice Dietitian's Business Card

A 2-sided business card for a dietitian (medical nutritionist) in private practice within a natural therapies allied health clinic. The business card needs to imply warmth and professionalism.
Target Market(s)
Doctors who may refer patients to a dietitian and patients themselves who may request dietetic assessment, education and counselling.
Industry/Entity Type
Business
Requirements
Must have
- The business card must be an intense blue on the front at the bottom, gradually lightening towards the top of the card. Please see:
http://example-pinboard.net/remy_hastwell/card-ideas/
for an example from "The quiet of the orchard" book. I'd like an apple tree on the left with a pale silver/grey trunk (like the silver in the book cover)and branches that bends over to the right above the writing. Apples to be a turquoise/aqua colour similar to that in "The quiet of the orchard" book cover. Front cover writing to read:
plateplan
0482 913 276
plateplan@kettlemail.net.au
'plateplan' is one word but I would like the 'my' in turquoise/aqua to match the apples and the 'dietitian' and the phone number and email address in the pale silver/grey to match the tree trunk.
I'd like the plateplan in larger font than the phone number and email address but for all 3 lines of text on the front of the business card to be stretched so they have the same left and right margin. (I hope this makes sense!)
I would like the back of the card to be white and the top section of text to be in the same turquoise/aqua from the apples on the front of the card and to read:
MAREE TOLBIN
Accredited Practising Dietitian (APD)
Bachelor of Health Science (Nutrition & Dietetics) - Honours
Master of Nutrition & Dietetics
This text should be stretched/compacted so that it all has the same left and right margin.
After this text there should be a blank line for spacing before the next section of text, which is to be in the silver/grey of the tree trunk. It should read:
Weight management
Diabetes
Impaired fasting glycaemia
Impaired glucose tolerance
Gestational diabetes
Wellness & general nutrition
Cardiovascular disease
high blood pressure
High cholesterol
High triglycerides
Fatty liver
Constipation
Diverticular disease
Coeliac disease
Irritable bowel syndrome
Gastroesophageal reflux
Lactose intolerance
Gout
Polycystic ovarian syndrome
Fertility
Pregnancy
Breastfeeding
Osteoporosis
Iron deficiency
Vegetarian eating
This set of text can run across the page from left to right and each medical condition could be separated from the next in some way to help with ease of reading. For example perhaps a space, dot and another space could separate the medical conditions. This set of text should be stretched so that the left and right margins of each line is the same. Thank you!
Nice to have
- An easy-to read but 'elegant' font would be nice - but I have no idea which one! Nothing too ornate, but not dull standard Times New Roman/Arial/Comic Sans either!
Should not have
- Times new roman/comic sans/arial fonts

```html
<!DOCTYPE html>
<html lang="en">
<head>
<meta charset="utf-8">
<title>plateplan – business card</title>
<link rel="stylesheet" href="https://fonts.googleapis.com/css2?family=PT+Sans:wght@400;700&display=swap">
<style>
  :root {
    --backdrop: #3a3a3c;
    --paper: #ffffff;
    --aqua: #3fb6c8;
    --aqua-soft: #63c9dc;
    --silver: #c3c6cc;
    --silver-light: #e2e5ea;
    --grey-text: #8c8e92;
    --blue-deep: #0b167a;
    --blue-mid: #1a2aa8;
    --blue-light: #2a3fc6;
    --card-shadow: rgba(0, 0, 0, 0.5);
  }
  * { box-sizing: border-box; margin: 0; padding: 0; }
  html, body {
    width: 1200px;
    height: 800px;
    overflow: hidden;
    background: var(--backdrop);
    font-family: "PT Sans", "Trebuchet MS", sans-serif;
  }
  .canvas {
    width: 1200px;
    height: 800px;
    display: flex;
    align-items: center;
    justify-content: center;
    gap: 40px;
  }
  .card {
    position: relative;
    width: 540px;
    height: 309px;
    box-shadow: 0 10px 30px var(--card-shadow);
    overflow: hidden;
  }

  /* Back of card */
  .card-back {
    background: var(--paper);
    padding: 32px 28px 24px 30px;
    display: flex;
    flex-direction: column;
    justify-content: space-between;
  }
  .credentials {
    color: var(--grey-text);
    font-size: 12px;
    line-height: 1.35;
  }
  .practitioner-name {
    color: var(--aqua);
    font-size: 19px;
    font-weight: 400;
    letter-spacing: 0.5px;
    margin-bottom: 1px;
  }
  .services {
    color: var(--grey-text);
    font-size: 11.5px;
    line-height: 1.5;
    text-align: justify;
    text-align-last: center;
  }

  /* Front of card */
  .card-front {
    background: radial-gradient(ellipse 80% 85% at 55% 40%, var(--blue-light) 0%, var(--blue-mid) 50%, var(--blue-deep) 100%);
  }
  .tree-artwork {
    position: absolute;
    left: 0;
    top: 14px;
    width: 192px;
    height: 244px;
    border-radius: 0 60% 45% 0 / 0 45% 55% 0;
    background:
      radial-gradient(circle at 76% 30%, var(--aqua-soft) 0 15%, rgba(99, 201, 220, 0) 16%),
      linear-gradient(160deg, rgba(195, 198, 204, 0.55) 0%, rgba(195, 198, 204, 0.28) 60%, rgba(195, 198, 204, 0.12) 100%);
  }
  .contact {
    position: absolute;
    left: 184px;
    top: 134px;
    width: 224px;
    text-align: right;
    color: var(--silver-light);
  }
  .brand-name {
    display: block;
    font-size: 45px;
    line-height: 1;
    letter-spacing: 0.5px;
    margin-bottom: 6px;
  }
  .contact-line {
    display: block;
    font-size: 15px;
    line-height: 1.2;
  }
</style>
</head>
<body>
  <main class="canvas">
    <section class="card card-back" aria-label="Back of business card">
      <div class="credentials">
        <h1 class="practitioner-name">MAREE TOLBIN</h1>
        <p>Accredited Practising Dietitian (APD)</p>
        <p>Bachelor of Health Science (Nutrition &amp; Dietetics) - Honours</p>
        <p>Master of Nutrition &amp; Dietetics</p>
      </div>
      <p class="services">Weight management - Diabetes - Impaired fasting glycaemia - Impaired glucose tolerance - Gestational diabetes - Wellness &amp; general nutrition - Cardiovascular disease - High blood pressure - High cholesterol - High triglycerides - Fatty liver - Constipation - Diverticular disease - Coeliac disease - Irritable bowel syndrome - Gastroesophageal reflux - Lactose intolerance - Gout - Polycystic ovarian syndrome - Fertility - Pregnancy - Breastfeeding - Osteoporosis - Iron deficiency - Vegetarian eating</p>
    </section>

    <section class="card card-front" aria-label="Front of business card">
      <div class="tree-artwork" role="img" aria-label="Silver scrolling apple tree branch curving to the right with a glossy aqua apple"></div>
      <div class="contact">
        <span class="brand-name">plateplan</span>
        <span class="contact-line">0482 913 276</span>
        <span class="contact-line">plateplan@kettlemail.net.au</span>
      </div>
    </section>
  </main>
</body>
</html>
```